Halvorsen Construction Needs a Business Card

Our current business card is very bland, and since we have a new logo, we would like a new business card design to reflect our company. It can be a single-sided or two-sided card, but it is important that our contact information appears on the same side. I am attaching a copy of our old card and our new logo. If you need the logo in another format than the one I'm sending, please let me know. This is the information that we must have on our card, but not necessarily in any specific order:
1) Our logo
2) General Contractor
3) Dale Halvorsen, Owner
4) 482 Commerce Ridge Road, Centre, Alabama 35871
5) Office: 256-555-0147
7) Fax: 256-555-0148
8) Cell: 256-555-0193
9) halvorsenconstruction@qvl-mail.net
10) halvorsenconstruction-example.com (can be omitted if necessary)
Also, I will need files in a format that I can alter if any of the above information changes in the near future. Thank you in advance for your submissions!
Target Market(s)
Commercial and residential clients, architects, and subcontractors.
Industry/Entity Type
Business
Look and feel

```html
<!DOCTYPE html>
<html lang="en">
<head>
<meta charset="utf-8">
<title>Halvorsen Construction – Business Card</title>
<link href="https://fonts.googleapis.com/css2?family=Roboto:wght@300;700&display=swap" rel="stylesheet">
<style>
  :root {
    --band-phone: #fdd22f;
    --band-web: #dec10c;
    --band-address: #e08000;
    --band-mail: #ff7f00;
    --ink: #111111;
    --paper: #ffffff;
    --faint: #dcdcdc;
  }
  * { margin: 0; padding: 0; box-sizing: border-box; }
  html, body { width: 741px; height: 1200px; overflow: hidden; background: var(--paper); }
  .card {
    position: relative; width: 741px; height: 1200px; overflow: hidden;
    background: var(--paper); font-family: "Roboto", "Helvetica Neue", Arial, sans-serif;
    font-weight: 300; color: var(--ink);
  }
  .contact-column { position: absolute; left: 0; top: 0; width: 325px; height: 1200px; }
  .band {
    position: absolute; left: 0; width: 325px; color: var(--paper);
    text-align: center; border-bottom: 2px solid var(--paper);
  }
  .band--phone { top: 0; height: 294px; background: var(--band-phone); }
  .band--web { top: 294px; height: 314px; background: var(--band-web); }
  .band--address { top: 608px; height: 316px; background: var(--band-address); }
  .band--mail { top: 924px; height: 276px; background: var(--band-mail); border-bottom: none; }
  .band__icon { position: absolute; left: 50%; transform: translateX(-50%); fill: var(--paper); }
  .band__text { position: absolute; left: 0; width: 100%; font-size: 25px; line-height: 36px; }
  .band--phone .band__icon { top: 30px; width: 50px; height: 50px; }
  .band--phone .band__text { top: 109px; }
  .band--web .band__icon { top: 28px; width: 50px; height: 50px; }
  .band--web .band__text { top: 143px; font-size: 19px; letter-spacing: -0.2px; }
  .band--address .band__icon { top: 24px; width: 40px; height: 70px; }
  .band--address .band__text { top: 111px; }
  .band--mail .band__icon { top: 22px; width: 62px; height: 40px; }
  .band--mail .band__text { top: 115px; }

  .brand {
    position: absolute; left: 330px; top: 60px; width: 405px; height: 82px;
    display: flex; align-items: center; gap: 14px;
  }
  .brand__square { width: 80px; height: 80px; background: var(--ink); flex: none; }
  .brand__name {
    font-weight: 700; font-size: 31px; line-height: 36px; color: var(--ink);
    text-transform: uppercase; letter-spacing: 1px;
  }
  .person { position: absolute; left: 325px; width: 416px; text-align: center; }
  .person__name { top: 282px; font-size: 54px; line-height: 64px; letter-spacing: -0.5px; }
  .person__title { top: 356px; font-size: 42px; line-height: 50px; }
  .trade { position: absolute; left: 325px; top: 548px; width: 416px; text-align: center; font-size: 55px; line-height: 58px; }
  .backdrop-shape {
    position: absolute; left: 395px; top: 745px; width: 420px; height: 440px;
    background: var(--faint); transform: rotate(8deg); opacity: 0.9;
  }
</style>
</head>
<body>
<div class="card">
  <div class="backdrop-shape" aria-hidden="true"></div>

  <div class="contact-column">
    <section class="band band--phone">
      <svg class="band__icon" viewBox="0 0 50 50" aria-hidden="true">
        <path d="M4 14c0-6 9-9 21-9s21 3 21 9v4h-10v-5c-3-1-7-1.5-11-1.5S17 12 14 13v5H4z"/>
        <path d="M16 19h18l8 12v14H8V31z"/>
      </svg>
      <p class="band__text">O (256) 555-0147<br>F (256) 555-0148<br>C (256) 555-0193</p>
    </section>
    <section class="band band--web">
      <svg class="band__icon" viewBox="0 0 50 50" aria-hidden="true" fill="none" stroke="#fff" stroke-width="3">
        <circle cx="25" cy="25" r="21"/>
        <ellipse cx="25" cy="25" rx="9" ry="21"/>
        <line x1="25" y1="4" x2="25" y2="46"/>
        <line x1="4" y1="25" x2="46" y2="25"/>
        <path d="M8 14h34M8 36h34"/>
      </svg>
      <p class="band__text">halvorsenconstruction-example.com</p>
    </section>
    <section class="band band--address">
      <svg class="band__icon" viewBox="0 0 40 70" aria-hidden="true">
        <path d="M20 0C9 0 0 9 0 20c0 14 20 50 20 50s20-36 20-50C40 9 31 0 20 0zm0 28a8 8 0 1 1 0-16 8 8 0 0 1 0 16z"/>
      </svg>
      <p class="band__text">482 Commerce Ridge Road,<br>Centre, Alabama<br>35871</p>
    </section>
    <section class="band band--mail">
      <svg class="band__icon" viewBox="0 0 62 40" aria-hidden="true">
        <path d="M0 0h62v40H0z"/>
        <path d="M2 2l29 22L60 2M2 38l20-20M60 38L40 18" fill="none" stroke="#ff7f00" stroke-width="2.5"/>
      </svg>
      <p class="band__text">halvorsenconstruction<br>@qvl-mail.net</p>
    </section>
  </div>

  <div class="brand">
    <div class="brand__square" aria-hidden="true"></div>
    <p class="brand__name">Halvorsen<br>Construction</p>
  </div>

  <h1 class="person person__name">Dale Halvorsen</h1>
  <p class="person person__title">Owner</p>
  <p class="trade">General<br>Contractor</p>
</div>
</body>
</html>
```